"Amberlane Vantage Harbor": unique end to end Chinese marketing and ecommerce solutions*

I would like to create a company website for my trademark: "Amberlane Vantage Harbor". We are based in Iceland. We are the only company in the market offering end-to-end Chinese digital marketing and eCommerce solutions. We help companies grow their brands and sales towards Chinese - whether tourism, export of products or services.
I include the logo that we have come up with in terms of colours and fonts.
The font is Trajan - I would like to use normal letters (capital and lowercase) for text.
Front page: Picture with colour filter. Logo in white. Text line underneath.
I am inspired by this website:
https://www.brindlecove.example/
I like these short videos for landing page:
https://www.pixelorchard.example/video/clip-48213907-misty-ridge-scenery
https://www.pixelorchard.example/video/clip-7390451128-4k-aerial-video-ridge-scenery
https://www.pixelorchard.example/video/clip-6620984315-ridge-scenery
Icelandic businesses looking for business opportunities in China or to attract Chinese tourists.
Digital Marketing

```html
<!DOCTYPE html>
<html lang="en">
<head>
<meta charset="utf-8">
<title>Amberlane Vantage Harbor</title>
<link href="https://fonts.googleapis.com/css2?family=Cinzel:wght@400;600&family=Open+Sans:wght@400;600&display=swap" rel="stylesheet">
<style>
:root{
  --blue:#0d4fa3;
  --blue-dark:#0a3f86;
  --gold:#b08a3e;
  --ink:#1c1c1c;
  --text:#333;
  --muted:#666;
  --light:#f6f6f6;
  --footer:#121212;
  --white:#fff;
}
*{box-sizing:border-box;margin:0;padding:0}
html,body{width:1200px;height:5310px;overflow:hidden}
body{position:relative;font-family:"Open Sans",Arial,sans-serif;color:var(--text);background:var(--white)}
.abs{position:absolute}
.serif{font-family:"Cinzel",Georgia,serif}
.btn{position:absolute;display:flex;align-items:center;justify-content:center;font-family:"Cinzel",Georgia,serif;font-size:16px;letter-spacing:.5px;color:var(--white);background:var(--blue);border-radius:3px}
.btn-outline{background:transparent;border:2px solid var(--white)}

/* hero */
.hero{position:absolute;left:0;top:0;width:1200px;height:610px;background:linear-gradient(170deg,#a98a55 0%,#7e7a6b 30%,#3d5f8f 60%,#1f4f96 100%)}
.brand{position:absolute;left:100px;top:22px;display:flex;align-items:center;gap:12px;color:var(--white)}
.brand-dot{width:40px;height:40px;border-radius:50%;border:2px solid var(--white)}
.brand-name{font-family:"Cinzel",serif;font-size:17px;line-height:1.1;width:200px}
.nav{position:absolute;top:30px;left:512px;display:flex;gap:32px;font-size:13px;color:var(--white)}
.hero h1{position:absolute;left:100px;top:160px;font-family:"Cinzel",serif;font-weight:400;font-size:52px;line-height:55px;color:var(--white)}
.hero-sub{position:absolute;left:100px;top:342px;width:460px;font-size:17px;line-height:28px;color:var(--white)}
.play{position:absolute;left:858px;top:240px;width:126px;height:126px;border-radius:50%;background:rgba(255,255,255,.25)}
.play-inner{position:absolute;left:30px;top:30px;width:66px;height:66px;border-radius:50%;background:var(--white)}
.dots{position:absolute;left:564px;top:562px;display:flex;gap:8px}
.dots span{width:11px;height:11px;border-radius:50%;border:2px solid var(--white)}
.dots span:first-child{background:var(--white)}

/* intro */
.center{position:absolute;left:0;width:1200px;text-align:center}
.section-title{font-family:"Cinzel",serif;font-weight:400;color:var(--ink)}
.intro-text{position:absolute;left:205px;top:755px;width:790px;text-align:center;font-size:17px;line-height:32px;color:var(--ink)}

/* clients */
.clients{position:absolute;left:0;top:1052px;width:1200px;height:402px;background:var(--light)}
.logos{position:absolute;left:100px;width:1000px;display:flex;justify-content:space-between;align-items:center}
.client{display:flex;align-items:center;gap:8px;font-family:"Open Sans",sans-serif;font-weight:600;font-size:16px;color:#555}
.client i{width:22px;height:22px;border-radius:50%;background:#777;display:block}

/* services */
.frame{position:absolute;width:78px;height:322px}
.frame.gold{background:var(--gold)}
.frame.blue{background:var(--blue)}
.photo{position:absolute;width:434px;height:286px}
.svc h2{position:absolute;font-family:"Cinzel",serif;font-weight:400;font-size:27px;color:var(--ink)}
.svc p{position:absolute;width:425px;font-size:13.5px;line-height:23px;color:#444}

/* meet */
.meet{position:absolute;left:0;top:3385px;width:1200px;height:423px;background:linear-gradient(180deg,#1d5cb0,#0d4fa3)}

/* guide */
.card{position:absolute;top:3970px;width:290px;height:300px;background:var(--white);box-shadow:0 2px 12px rgba(0,0,0,.1)}
.card .thumb{position:absolute;left:10px;top:10px;width:270px;height:175px}
.card .date{position:absolute;left:10px;top:198px;font-size:11px;color:#444}
.card .title{position:absolute;left:10px;top:222px;width:272px;font-size:14px;font-weight:600;line-height:22px;color:var(--ink)}
.card .more{position:absolute;left:10px;top:288px;font-family:"Cinzel",serif;font-size:13px;color:var(--blue)}
.arrow-box{position:absolute;width:36px;height:36px;background:var(--white);box-shadow:0 1px 6px rgba(0,0,0,.15);display:flex;align-items:center;justify-content:center}

/* form */
.field{position:absolute;left:310px;width:282px;height:42px;border:1px solid #ccc;font-size:12.5px;color:#555;padding:12px 14px}
.field em{color:#d33;font-style:normal}
.hl{color:var(--blue);font-weight:600}

/* footer */
.footer{position:absolute;left:0;top:4955px;width:1200px;height:355px;background:var(--footer);color:var(--white)}
.footer h4{position:absolute;top:66px;font-family:"Cinzel",serif;font-weight:400;font-size:16px}
.footer ul{position:absolute;top:100px;list-style:none;font-size:12.5px;line-height:22px}
.social{position:absolute;left:785px;top:100px;display:flex;gap:10px}
.social span{width:16px;height:16px;border-radius:50%;background:var(--white)}
</style>
</head>
<body>

<header class="hero" role="img" aria-label="Misty mountain ridge with an ancient wall at sunrise, tinted blue">
  <div class="brand"><span class="brand-dot"></span><span class="brand-name">Amberlane Vantage Harbor</span></div>
  <nav class="nav"><span>Home</span><span>About</span><span>Services ⌄</span><span>Clients</span><span>Blog</span><span>Contact</span><span>☏ (555) - 014 - 2290</span></nav>
  <h1>REACH YOUR<br>CHINESE<br>CUSTOMERS.</h1>
  <p class="hero-sub">Hands-on, effective and affordable China marketing solutions.</p>
  <div class="btn btn-outline" style="left:100px;top:414px;width:174px;height:46px;font-size:15px">CHINA BASED</div>
  <div class="play"><div class="play-inner"><svg width="66" height="66"><circle cx="33" cy="33" r="19" fill="var(--blue)"/><path d="M28 23 L43 33 L28 43Z" fill="#fff"/></svg></div></div>
  <svg class="abs" style="left:60px;top:288px" width="20" height="36"><path d="M16 2 L4 18 L16 34" stroke="#fff" stroke-width="2" fill="none"/></svg>
  <svg class="abs" style="left:1120px;top:288px" width="20" height="36"><path d="M4 2 L16 18 L4 34" stroke="#fff" stroke-width="2" fill="none"/></svg>
  <div class="dots"><span></span><span></span><span></span><span></span></div>
</header>

<section>
  <h2 class="center section-title" style="top:700px;font-size:33px">MARKETING FOR RESULTS, NOT FOR SHOW.</h2>
  <p class="intro-text">Lorem ipsum dolor sit amet, consectetur adipiscing elit, sed do eiusmod tpor incididunt ut labore et dolore magna aliqua. uis pm suspendisse ultrices gravids commodo virra aeces accmsan lacus vel facilisis. Lorem ipsum dolor sit amet, consectetur adipiscing elitLorem ipsum dolor sit amet, consectetur ased do eiusmod tempor incididunt ut labore et dolore magna aliqua.</p>
  <div class="btn" style="left:488px;top:947px;width:224px;height:44px">READ MORE ABOUT US</div>
</section>

<section class="clients">
  <h2 class="center section-title" style="top:78px;font-size:25px">100+ CLIENTS FROM OUR COUNTRIES</h2>
  <div class="logos" style="top:180px">
    <span class="client"><i></i>Northfern Plots</span>
    <span class="client">Wexmoor</span>
    <span class="client"><i></i>Quillray</span>
    <span class="client">Tarnby Hollis Group</span>
    <span class="client"><i></i>Cobalt Nest Relief</span>
  </div>
  <div class="btn" style="left:467px;top:270px;width:266px;height:43px">READ CUSTOMER STORIES</div>
</section>

<section class="svc">
  <div class="frame gold" style="left:140px;top:1537px"></div>
  <div class="photo" role="img" aria-label="Team of young colleagues working together around a laptop" style="left:158px;top:1556px;background:linear-gradient(135deg,#d8d2c8,#8a7a6a 55%,#3b3b40)"></div>
  <h2 style="left:645px;top:1585px">DIGITAL MARKETING</h2>
  <p style="left:645px;top:1638px">Lorem ipsum dolor sit amet, consectetur adipiscing elit, sed do eiusmod tempor incididunt ut labore et dolore magna aliqua.is ipsum suspendisse ultrices gravida. Risus commodo viverra maecenas accumsan lacus vel facilisis.</p>
  <div class="btn" style="left:645px;top:1761px;width:148px;height:44px">READ MORE</div>

  <h2 style="left:140px;top:1935px">ECOMMERCE SOLUTIONS</h2>
  <p style="left:140px;top:1988px">Lorem ipsum dolor sit amet, consectetur adipiscing elit, sed do eiusmod tempor incididunt ut labore et dolore magna aliqua.is ipsum suspendisse ultrices gravida. Risus commodo viverra maecenas accumsan lacus vel facilisis.</p>
  <div class="btn" style="left:143px;top:2111px;width:148px;height:44px">READ MORE</div>
  <div class="frame blue" style="left:988px;top:1888px"></div>
  <div class="photo" role="img" aria-label="Laptop showing an online shop on a white desk with pencils and a plant" style="left:614px;top:1906px;background:linear-gradient(135deg,#f2f2f2,#d9d9d9 60%,#b9b9b9)"></div>

  <div class="frame gold" style="left:140px;top:2250px"></div>
  <div class="photo" role="img" aria-label="Three young travellers smiling beside a tent in a forest" style="left:158px;top:2269px;background:linear-gradient(135deg,#a59c88,#c86a34 50%,#6f6a5c)"></div>
  <h2 style="left:645px;top:2298px">TOURISM</h2>
  <p style="left:645px;top:2351px">Lorem ipsum dolor sit amet, consectetur adipiscing elit, sed do eiusmod tempor incididunt ut labore et dolore magna aliqua.is ipsum suspendisse ultrices gravida. Risus commodo viverra maecenas accumsan lacus vel facilisis.</p>
  <div class="btn" style="left:645px;top:2474px;width:148px;height:44px">READ MORE</div>

  <h2 style="left:140px;top:2648px">EXPORT OF PRODUCTS</h2>
  <p style="left:140px;top:2701px">Lorem ipsum dolor sit amet, consectetur adipiscing elit, sed do eiusmod tempor incididunt ut labore et dolore magna aliqua.is ipsum suspendisse ultrices gravida. Risus commodo viverra maecenas accumsan lacus vel facilisis.</p>
  <div class="btn" style="left:143px;top:2824px;width:148px;height:44px">READ MORE</div>
  <div class="frame blue" style="left:988px;top:2600px"></div>
  <div class="photo" role="img" aria-label="Warehouse worker checking cardboard boxes on shelves" style="left:614px;top:2619px;background:linear-gradient(135deg,#e7e7ea,#c9a57c 60%,#8c6b4a)"></div>

  <div class="frame gold" style="left:140px;top:2962px"></div>
  <div class="photo" role="img" aria-label="Woman looking at her phone under red night lights" style="left:158px;top:2981px;background:linear-gradient(135deg,#2a1a1a,#8c2020 45%,#1a1a22)"></div>
  <h2 style="left:645px;top:3010px">INFLUENCER MARKETING</h2>
  <p style="left:645px;top:3063px">Lorem ipsum dolor sit amet, consectetur adipiscing elit, sed do eiusmod tempor incididunt ut labore et dolore magna aliqua.is ipsum suspendisse ultrices gravida. Risus commodo viverra maecenas accumsan lacus vel facilisis.</p>
  <div class="btn" style="left:645px;top:3186px;width:148px;height:44px">READ MORE</div>
</section>

<section class="meet" role="img" aria-label="Office team meeting, tinted blue">
  <h2 class="center serif" style="top:106px;font-weight:400;font-size:40px;color:#fff">MEET US IN CHINA.</h2>
  <p class="center" style="top:178px;font-size:19px;line-height:31px;color:#fff">Our sales representatives travel around&nbsp; China constantly. Book an appointment<br>and we’ll meet you at your office.</p>
  <div class="btn btn-outline" style="left:469px;top:255px;width:262px;height:46px">BOOK AN APPOINTMENT</div>
</section>

<section>
  <p class="center" style="top:3855px;font-size:15px;color:var(--gold)">OUR FREE GUIDE</p>
  <p class="center serif" style="top:3888px;font-size:14px;line-height:23px;color:var(--ink)">OUR EXPERIENCED TEAM REGULARLY PRODUCE NEW&nbsp; CONTENT TO HELP OUR AWESOME<br>COMMUNITY OF MARKETING AND SALES PRODESSIONALS.IMPROVE THEIR SKILLS.</p>
  <div class="abs" style="left:0;top:4111px;width:1200px;height:1px;background:#e5e5e5"></div>
  <div class="arrow-box" style="left:80px;top:4035px"><svg width="10" height="16"><path d="M8 1 L2 8 L8 15" stroke="#b08a3e" stroke-width="1.5" fill="none"/></svg></div>
  <div class="arrow-box" style="left:1082px;top:4035px"><svg width="10" height="16"><path d="M2 1 L8 8 L2 15" stroke="#b08a3e" stroke-width="1.5" fill="none"/></svg></div>
  <article class="card" style="left:142px"><div class="thumb" role="img" aria-label="Colleagues reviewing notes on a glass wall" style="background:linear-gradient(135deg,#c7d3dc,#6f7e8c)"></div><p class="date">December 20,2020</p><p class="title">Lorem ipsum dolor sit&nbsp; consectetur adipiscing elit, sed do eiusmod tempor incididunt ut labore et</p><p class="more">LEARN MORE</p></article>
  <article class="card" style="left:455px"><div class="thumb" role="img" aria-label="Small team discussing at an office desk" style="background:linear-gradient(135deg,#d6e2ea,#7a8a94)"></div><p class="date">December 20,2020</p><p class="title">Lorem ipsum dolor sit&nbsp; consectetur adipiscing elit, sed do eiusmod tempor incididunt ut labore et</p><p class="more">LEARN MORE</p></article>
  <article class="card" style="left:768px"><div class="thumb" role="img" aria-label="Woman working on a laptop in a bright office" style="background:linear-gradient(135deg,#e4e7ea,#9aa3ad)"></div><p class="date">December 20,2020</p><p class="title">Lorem ipsum dolor sit&nbsp; consectetur adipiscing elit, sed do eiusmod tempor incididunt ut labore et</p><p class="more">LEARN MORE</p></article>
</section>

<section>
  <h2 class="center section-title" style="top:4405px;font-size:34px">GROW YOUR BUSINESS NOW</h2>
  <p class="center" style="top:4468px;font-size:15px;line-height:27px;color:var(--ink);font-weight:600">If you’re interested in generating more <span class="hl">sales</span>, increasing <span class="hl">traffic</span> and attracting <span class="hl">higher</span> quality leads,<br>then sign up to receive a No-obligation <span class="hl">FREE</span> Strategy Session</p>
  <div class="field" style="top:4560px">Full Name<em>*</em></div>
  <div class="field" style="top:4610px">Email Address<em>*</em></div>
  <div class="field" style="top:4660px">Phone Number<em>*</em></div>
  <div class="field" style="top:4711px">Please select Service<span style="float:right">⌄</span></div>
  <div class="field" style="left:605px;top:4560px;height:136px">Write your Message<em>*</em></div>
  <div class="btn" style="left:605px;top:4707px;width:283px;height:44px;border-radius:0;font-size:15px">SUBMIT NOW&nbsp;
    <svg width="14" height="14"><path d="M1 7 L13 1 L9 13 L7 8Z" fill="#fff"/></svg></div>
  <div class="logos" style="top:4868px">
    <span class="client"><i></i>Northfern Plots</span>
    <span class="client">Wexmoor</span>
    <span class="client"><i></i>Quillray</span>
    <span class="client">Tarnby Hollis Group</span>
    <span class="client"><i></i>Cobalt Nest Relief</span>
  </div>
</section>

<footer class="footer">
  <h4 style="left:100px">NAVIGATION</h4>
  <ul style="left:100px"><li>Home</li><li>About</li><li>Services</li><li>Clients</li><li>Blog</li><li>Contact Us</li></ul>
  <h4 style="left:280px">SERVICES</h4>
  <ul style="left:280px"><li>Digital marketing</li><li>eCommerce solutions</li><li>Tourism</li><li>Export of products</li><li>Influencer Marketing</li><li>Market Entry</li></ul>
  <h4 style="left:485px">CONTACT US</h4>
  <ul style="left:485px"><li>⌖ 48 Lindqvist Lane</li><li>&nbsp;&nbsp;&nbsp;Reykholt 311</li><li>☏ (555) 014 2290</li><li>&nbsp;</li><li>✉ info@amberlanevantageharbor.example</li></ul>
  <h4 style="left:785px">FOLLOW US ON</h4>
  <div class="social"><span></span><span></span><span></span><span></span></div>
  <p class="abs serif" style="left:930px;top:110px;width:170px;font-size:18px;line-height:24px;text-align:right">Amberlane Vantage Harbor</p>
  <div class="abs" style="left:100px;top:278px;width:1000px;height:1px;background:#333"></div>
  <p class="center" style="top:300px;font-size:12px">© 2020 Amberlane Vantage Harbor. All Rights Reserved.</p>
</footer>

</body>
</html>
```